ZOQ

We need to design a power point presentation that can englobe all our company products.

This presentation has to have all the required to be used as template for future presentations.

We focus on prodcut developing for supermarkets, ( we help them with their own brand products ex. Sunny Pantry, KD, etc.)
Also we are on the marine industry, we develop ships and oil rigs for the Oil and deep water market.

Target Market(s)

Oil Companies
Supermarket companies
Retail Companies

Industry/Entity Type

It Company

Requirements
Must have
• Our Logo and company colors
Nice to have
• Something describing globalization.
Should not have
• Orange color

```html
<!DOCTYPE html>
<html lang="es">
<head>
<meta charset="utf-8">
<title>Strategic Review 2014 – Navora Marine Solutions</title>
<link href="https://fonts.googleapis.com/css2?family=Open+Sans:wght@300;400;600;700&display=swap" rel="stylesheet">
<style>
:root{
  --navy:#0b3a73;
  --blue:#1a9ad6;
  --sky:#3fc0ee;
  --pale:#d9f1fb;
  --green:#5bb531;
  --lime:#a9d86e;
  --ink:#333;
  --grey:#555;
  --line:#1a9ad6;
  --slate:#5b75b3;
  --track:#555;
}
*{box-sizing:border-box;margin:0;padding:0}
html,body{width:1067px;height:1200px;overflow:hidden;background:#fff}
body{font-family:"Open Sans",Arial,sans-serif;color:var(--ink)}
.deck{display:grid;grid-template-columns:533px 534px;grid-template-rows:400px 400px 400px;width:1067px;height:1200px}
.slide{position:relative;overflow:hidden;background:#fff;border-right:1px solid var(--line);border-bottom:1px solid var(--line)}
.slide:nth-child(even){border-right:none}
.deco{position:absolute;inset:0;width:100%;height:100%}
.slide-title{position:absolute;left:20px;top:14px;font-size:19px;font-weight:300;color:var(--navy);letter-spacing:.3px}
.slide-tag{position:absolute;right:20px;top:20px;font-size:10px;font-weight:400;color:var(--green)}
.slide-tag b{font-weight:700;color:var(--blue)}
.rule{position:absolute;left:20px;right:20px;top:38px;height:1px;background:var(--blue)}
.rule::before{content:"";position:absolute;left:6px;top:0;width:6px;height:6px;border-right:1px solid var(--blue);border-bottom:1px solid var(--blue);transform:rotate(45deg) translate(-2px,-3px);background:#fff}
.brand{position:absolute;display:flex;align-items:center;gap:4px;color:var(--navy);font-weight:400;line-height:1}
.brand .dot{width:7px;height:7px;border-radius:50%;background:var(--navy)}
.brand .name{font-size:11px;letter-spacing:.5px}
.brand.corner{left:12px;bottom:14px}
/* cover */
.cover-globe{position:absolute;left:270px;top:-40px;width:300px;height:300px;border-radius:50%;background:radial-gradient(circle at 45% 45%,#7fd3f2,#1a74b8 55%,#0b2a5a)}
.cover-title{position:absolute;left:38px;top:322px;font-size:23px;font-weight:300;color:var(--navy)}
.cover-title b{font-size:15px;font-weight:700;color:var(--blue)}
.cover-sub{position:absolute;left:38px;top:350px;font-size:10.5px;font-weight:300;color:var(--grey)}
.cover-seal{position:absolute;left:392px;top:290px;width:180px;height:180px;border-radius:50%;background:#fff}
.brand.cover-brand{left:432px;top:350px}
.brand.cover-brand .name{font-size:15px}
/* spec table */
.spec-head{position:absolute;left:22px;top:55px;font-size:11px;font-weight:300;color:var(--blue)}
.spec-head b{font-weight:700}
.spec-sub{position:absolute;left:34px;top:72px;font-size:6px;font-weight:700;color:var(--ink)}
.spec{position:absolute;top:95px;width:140px;border-collapse:collapse;font-size:4.6px;text-transform:uppercase}
.spec td{height:11px;border-bottom:1px solid #9fd6ee;padding:0 2px;color:var(--ink)}
.spec td.v{text-align:right;font-weight:700;background:#e8f6fc;width:38px}
.spec tr:first-child td{border-top:2px solid var(--blue)}
.spec.a{left:33px}.spec.b{left:213px;width:150px}
.shot{position:absolute;border-radius:50%}
.shot.s1{left:455px;top:45px;width:106px;height:106px;background:radial-gradient(#f2f2f2,#8a8f96)}
.shot.s2{left:373px;top:172px;width:76px;height:76px;background:radial-gradient(#c9ced4,#5e6d78)}
.shot.s3{left:418px;top:258px;width:124px;height:124px;background:radial-gradient(#f3e3cf,#b8824e)}
.shot.s4{left:315px;top:321px;width:86px;height:86px;background:linear-gradient(#dfe6ea,#8a939a)}
/* company */
.lead{position:absolute;left:20px;top:79px;width:490px;font-size:10.5px;font-weight:300;color:var(--blue);text-transform:uppercase;line-height:1.3}
.lead b{font-weight:700}
.body{position:absolute;left:20px;width:495px;font-size:8.3px;line-height:1.35;color:var(--ink)}
.body b{font-weight:700}
.body.p1{top:129px}.body.p2{top:231px}
.hr{position:absolute;left:20px;top:189px;width:174px;height:1px;background:#aaa}
.sub-lead{position:absolute;left:20px;top:208px;font-size:10.5px;font-weight:300;color:var(--blue);text-transform:uppercase}
.sub-lead b{font-weight:700}
/* timeline */
.tl-kicker{position:absolute;left:20px;top:61px;font-size:11px;font-weight:300;text-transform:uppercase;color:var(--ink)}
.tl-head{position:absolute;left:20px;top:76px;font-size:16px;font-weight:700;color:var(--blue);text-transform:uppercase}
.stage{position:absolute;top:133px;width:88px;height:108px;padding:4px;color:#fff;font-size:7px;line-height:1.2;text-transform:uppercase}
.stage .avail{position:absolute;left:3px;right:3px;bottom:3px;height:41px;background:#fff;color:var(--ink);font-size:5.6px;font-weight:600;padding:22px 4px 0}
.st1{left:20px;background:var(--navy)}.st2{left:121px;background:var(--slate)}.st3{left:222px;background:var(--green)}.st4{left:324px;background:var(--blue)}.st5{left:425px;background:#7fd0f2}
.track{position:absolute;left:20px;right:20px;top:257px;height:9px;background:var(--track)}
.year{position:absolute;top:257px;font-size:6.5px;color:#fff;line-height:9px}
.node{position:absolute;top:252px;width:19px;height:19px;border-radius:50%;background:var(--track)}
.node::after{content:"";position:absolute;inset:5px;border-radius:50%;background:#fff}
/* product lists */
.plist{position:absolute;top:62px;list-style:none;font-size:8.2px;color:var(--ink);line-height:1.3}
.plist li{position:relative;padding:0 0 5px 8px;margin-bottom:5px;border-bottom:1px dotted #bbb;width:190px}
.plist li:last-child{border-bottom:none}
.plist li::before{content:"›";position:absolute;left:0;top:-2px;font-size:11px;color:var(--blue)}
.plist.left{left:31px}.plist.right{left:259px;width:220px}
.plist.right li{width:220px}
/* closing */
.thanks{position:absolute;left:0;right:0;top:172px;text-align:center;font-size:29px;font-weight:300;color:var(--blue)}
.thanks-sub{position:absolute;left:0;right:0;top:210px;text-align:center;font-size:11px;font-weight:300;color:var(--grey)}
</style>
</head>
<body>
<main class="deck">

  <!-- Cover -->
  <section class="slide cover">
    <svg class="deco" viewBox="0 0 533 400" aria-hidden="true">
      <defs>
        <linearGradient id="coverSky" x1="0" y1="0" x2="1" y2="1"><stop offset="0" stop-color="#bfe9fa"/><stop offset="1" stop-color="#e9f8fd"/></linearGradient>
        <linearGradient id="coverBlue" x1="0" y1="0" x2="1" y2="0"><stop offset="0" stop-color="#1a74c8"/><stop offset="1" stop-color="#3fc0ee"/></linearGradient>
      </defs>
      <rect width="533" height="290" fill="url(#coverSky)"/>
      <path d="M0 0H533V240C420 210 300 150 0 110Z" fill="#8fd8f5"/>
      <path d="M0 110C180 150 330 210 460 280L430 282C300 230 150 190 0 170Z" fill="url(#coverBlue)"/>
      <path d="M0 170C150 190 300 230 430 282L420 285C280 250 140 230 0 225Z" fill="#0b3a73"/>
      <path d="M0 205C150 225 300 255 440 285L430 288C280 265 130 250 0 245Z" fill="var(--green)"/>
      <path d="M0 245C140 255 290 270 430 288C300 286 150 280 0 280Z" fill="#ffffff"/>
      <path d="M0 280H533V400H0Z" fill="#fff"/>
    </svg>
    <div class="cover-globe" role="img" aria-label="Glowing Earth globe with network light trails across the Americas"></div>
    <div class="cover-seal"></div>
    <h1 class="cover-title">STRATEGIC REVIEW <b>2014</b></h1>
    <p class="cover-sub">Alex Rivera, 1 January 2014</p>
    <div class="brand cover-brand"><span class="dot"></span><span class="name">NAVORA MARINE</span></div>
  </section>

  <!-- Products: specs -->
  <section class="slide specs">
    <svg class="deco" viewBox="0 0 533 400" aria-hidden="true">
      <path d="M0 300L45 338L0 342Z" fill="var(--green)"/>
      <path d="M0 330L45 338L0 345Z" fill="var(--lime)"/>
      <path d="M40 340L220 400H120Z" fill="var(--sky)"/>
    </svg>
    <h2 class="slide-title">PRODUCTOS</h2>
    <p class="slide-tag">STRATEGIC REVIEW <b>2014</b></p>
    <div class="rule"></div>
    <p class="spec-head">PLATAFORMAS DE <b>PERFORACIÓN SEMISUMERGIBLES</b></p>
    <p class="spec-sub">DIMENSIONES</p>
    <table class="spec a">
      <tr><td>Largo total</td><td class="v">104,5 M</td></tr>
      <tr><td>Ancho total</td><td class="v">70,5 M</td></tr>
      <tr><td>Largo cubierta principal</td><td class="v">83,1 M</td></tr>
      <tr><td>Ancho cubierta principal</td><td class="v">69,5 M</td></tr>
      <tr><td>Helideck (diámetro)</td><td class="v">27,75 M</td></tr>
      <tr><td>Moonpool dimensiones</td><td class="v">21,95 M X 7 M</td></tr>
      <tr><td>Calado</td><td class="v"></td></tr>
      <tr><td>Calado para operación</td><td class="v">17,5 M</td></tr>
      <tr><td>Calado de supervivencia</td><td class="v">5,5 M</td></tr>
      <tr><td>Calado de tránsito</td><td class="v">9,75 M</td></tr>
      <tr><td>Desplazamiento</td><td class="v"></td></tr>
      <tr><td>Desplazamiento operativo</td><td class="v">40710 M.T.</td></tr>
      <tr><td>Desplazamiento de supervivencia</td><td class="v">38759 M.T.</td></tr>
      <tr><td>Desplazamiento en tránsito</td><td class="v">30830 M.T.</td></tr>
      <tr><td>Profundidad operacional</td><td class="v">100 – 1500 M.</td></tr>
      <tr><td>Capacidades de almacenaje</td><td class="v"></td></tr>
      <tr><td>Balastra de agua</td><td class="v">13000 M.</td></tr>
      <tr><td>Combustible</td><td class="v">3200 M.</td></tr>
    </table>
    <table class="spec b">
      <tr><td>Agua de perforación</td><td class="v">1360 M.</td></tr>
      <tr><td>Agua potable</td><td class="v">800 M.</td></tr>
      <tr><td>Lodos líquidos activos (superficie)</td><td class="v">750 M.</td></tr>
      <tr><td>Lodos líquidos de</td><td class="v">1170 M.</td></tr>
      <tr><td>Reserva (columna/pontón)</td><td class="v">400 M.</td></tr>
      <tr><td>Bentonita/barita en groso</td><td class="v">400 M.</td></tr>
      <tr><td>Cemento en groso</td><td class="v">1050 M.</td></tr>
      <tr><td>Aceite base</td><td class="v">1160 M.</td></tr>
      <tr><td>Salmuera</td><td class="v">350 M.</td></tr>
      <tr><td>Aguas negras</td><td class="v">5000 M.T.</td></tr>
      <tr><td>Carga variable</td><td class="v">10 KNOTS</td></tr>
      <tr><td>Velocidad de tránsito</td><td class="v"></td></tr>
    </table>
    <div class="shot s1" role="img" aria-label="3D rendering of drilling rig deck equipment"></div>
    <div class="shot s2" role="img" aria-label="Photo of pipework inside a rig module"></div>
    <div class="shot s3" role="img" aria-label="Photo of a rig derrick structure"></div>
    <div class="shot s4" role="img" aria-label="Rendering of a semisubmersible platform at sea"></div>
    <div class="brand corner"><span class="dot"></span><span class="name">NAVORA</span></div>
  </section>

  <!-- Company -->
  <section class="slide company">
    <svg class="deco" viewBox="0 0 533 400" aria-hidden="true">
      <path d="M0 300L45 338L0 342Z" fill="var(--green)"/>
      <path d="M0 330L45 338L0 345Z" fill="var(--lime)"/>
      <path d="M40 340L220 400H120Z" fill="var(--sky)"/>
    </svg>
    <h2 class="slide-title">NUESTRA EMPRESA</h2>
    <p class="slide-tag">STRATEGIC REVIEW <b>2014</b></p>
    <div class="rule"></div>
    <p class="lead">Está dedicada principalmente a brindar soluciones en el sector <b>marítimo petrolero, enfocándonos</b> en productos de vanguardia que se adapten a las necesidades en dicho sector.</p>
    <p class="body p1">Buscamos la mejora continua de nuestros servicios, procesos y productos. Generamos sinergia de forma internacional, acercando a las grandes corporaciones y empresas de <b>CHINA,</b> facilitando los procesos de incorporación de éstas al mercado de exploración, producción, construcción, avituallamiento y mantenimiento marítimo del sector petrolero, en aguas profundas y cuencas del sureste del <b>GOLFO DE MÉXICO.</b></p>
    <div class="hr"></div>
    <p class="sub-lead">Al estar posicionados en <b>Hong Kong y Beijing</b></p>
    <p class="body p2">Nos permite enlazar y trabajar con fabricantes y constructores que cubren las necesidades con estándares internacionales de calidad y garantía a satisfacción del sector marítimo petrolero, garantizando y fortaleciendo la orientación para nuestros clientes, en la gestión de las negociaciones y logrando que las operaciones sean seguras y confiables, maximizando así el valor de las oportunidades.</p>
    <div class="brand corner"><span class="dot"></span><span class="name">NAVORA</span></div>
  </section>

  <!-- Timeline -->
  <section class="slide timeline">
    <svg class="deco" viewBox="0 0 534 400" aria-hidden="true">
      <path d="M0 300L45 338L0 342Z" fill="var(--green)"/>
      <path d="M0 330L45 338L0 345Z" fill="var(--lime)"/>
      <path d="M40 340L220 400H120Z" fill="var(--sky)"/>
    </svg>
    <h2 class="slide-title">PRODUCTOS</h2>
    <p class="slide-tag">STRATEGIC REVIEW <b>2014</b></p>
    <div class="rule"></div>
    <p class="tl-kicker">Disponibilidad inmediata de</p>
    <p class="tl-head">Proyectos en desarrollo-2014</p>
    <div class="stage st1">Plataformas de perforación semisumergibles<div class="avail">Disponibilidad<br>4 unidades</div></div>
    <div class="stage st2">Barcos grúa semi-sumergibles con avituallamiento<div class="avail">Disponibilidad<br>1 unidad</div></div>
    <div class="stage st3">Plataformas jack-ups súper M2<div class="avail">Disponibilidad<br>4 unidades</div></div>
    <div class="stage st4">Plataformas jack-ups para 400 pies de profundidad con capacidad de perforación de 30,000 pies<div class="avail">Disponibilidad<br>3 unidades</div></div>
    <div class="stage st5">Carriers semisumergibles de alto tonelaje<div class="avail">Disponibilidad<br>4 unidades</div></div>
    <div class="track"></div>
    <span class="year" style="left:35px">1980</span><span class="node" style="left:55px"></span>
    <span class="year" style="left:136px">1990</span><span class="node" style="left:156px"></span>
    <span class="year" style="left:237px">2000</span><span class="node" style="left:257px"></span>
    <span class="year" style="left:339px">2010</span><span class="node" style="left:359px"></span>
    <span class="year" style="left:440px">2014</span><span class="node" style="left:460px"></span>
    <div class="brand corner"><span class="dot"></span><span class="name">NAVORA</span></div>
  </section>

  <!-- Product list -->
  <section class="slide catalogue">
    <svg class="deco" viewBox="0 0 533 400" aria-hidden="true">
      <path d="M0 315L30 345L0 348Z" fill="var(--green)"/>
      <path d="M0 340L30 345L0 350Z" fill="var(--lime)"/>
      <path d="M25 348L200 400H100Z" fill="var(--sky)"/>
    </svg>
    <h2 class="slide-title" style="left:6px">PRODUCTOS</h2>
    <p class="slide-tag" style="right:34px">STRATEGIC REVIEW <b>2014</b></p>
    <div class="rule" style="left:6px;right:34px"></div>
    <ul class="plist left">
      <li>Plataformas de<br>Exploración y Perforación</li>
      <li>Plataformas de<br>Perforación (Jack-Ups)</li>
      <li>Plataformas para Aguas Profundas<br>Semisumergibles de Última Generación</li>
      <li>Plataformas Semisumergibles de<br>Posicionamiento Dinámico</li>
      <li>Plataformas de Producción</li>
      <li>Plataformas Habitacionales</li>
      <li>Barcos de Exploración,<br>Producción y Almacenamiento Propio</li>
      <li>Barcos Grúa</li>
      <li>Barcos Multipropósito de<br>Posicionamiento Dinámico</li>
    </ul>
    <ul class="plist right">
      <li>Barcos Contra Incendios</li>
      <li>Barcos Contra Incendios de<br>Posicionamiento Dinámico</li>
      <li>Remolcadores Transportadores</li>
      <li>Mini Abastecedores para transporte de material</li>
      <li>Abastecedores de Nueva Generación<br>para transporte de Material</li>
      <li>Lanchas Rápidas para transporte de<br>personal y equipo ligero</li>
      <li>Abastecedores Rápidos para el<br>transporte de Material</li>
      <li>Abastecedores remolcadores</li>
      <li>Abastecedor de Rápida Intervención</li>
      <li>Abastecedor de Nueva Generación para<br>Transporte de Contenedores Refrigerados y Secos</li>
      <li>Gangways<br>Refacciones de Nuestros Productos</li>
    </ul>
    <div class="brand corner" style="left:2px"><span class="dot"></span><span class="name">NAVORA</span></div>
  </section>

  <!-- Closing -->
  <section class="slide closing">
    <svg class="deco" viewBox="0 0 534 400" aria-hidden="true">
      <defs>
        <linearGradient id="closeSky" x1="0" y1="0" x2="0" y2="1"><stop offset="0" stop-color="#d9f1fb"/><stop offset=".5" stop-color="#ffffff"/><stop offset="1" stop-color="#ffffff"/></linearGradient>
        <linearGradient id="closeBlue" x1="0" y1="0" x2="1" y2="0"><stop offset="0" stop-color="#1a9ad6"/><stop offset="1" stop-color="#3fc0ee"/></linearGradient>
      </defs>
      <rect width="534" height="400" fill="url(#closeSky)"/>
      <path d="M0 245C120 300 300 330 534 330V400H0Z" fill="url(#closeBlue)"/>
      <path d="M0 280C150 330 330 345 534 320V400H0Z" fill="#8fd8f5"/>
      <path d="M230 330C360 320 460 290 534 260V275C450 310 350 335 230 335Z" fill="var(--lime)"/>
      <path d="M0 330C170 360 360 360 534 340V400H0Z" fill="#d4f0fb"/>
    </svg>
    <p class="thanks">Thanks For Listening</p>
    <p class="thanks-sub">Alex Rivera, 1 January 2014</p>
  </section>

</main>
</body>
</html>
```